Business Card Design for Property Development Company Director

I am looking for a professional and unforgettable business card design for our Director of our Property Development Company.
Please see attached .pptx file to find out what information to include. You don't have to follow the exact format shown in the file - I am interested to see your creative flair using the information provided.

```html
<!DOCTYPE html>
<html lang="en">
<head>
<meta charset="utf-8">
<title>Kestrel Property Group – Business Card</title>
<link rel="stylesheet" href="https://fonts.googleapis.com/css2?family=Roboto:wght@400;500;700&family=Roboto+Condensed:wght@700&display=swap">
<style>
  :root {
    --bg: #e4e4e6;
    --brand-blue: #2a4c8c;
    --ink-dark: #4a4b4f;
    --ink-mid: #5c5d61;
    --paper: #f4f4f5;
    --panel: #e6e6e8;
    --white: #ffffff;
  }
  * { box-sizing: border-box; margin: 0; padding: 0; }
  html, body { width: 1200px; height: 726px; overflow: hidden; }
  body {
    background: var(--bg);
    font-family: "Roboto", Arial, sans-serif;
    position: relative;
  }
  .card {
    position: absolute;
    top: 213px;
    width: 525px;
    height: 300px;
    border-radius: 3px;
    overflow: hidden;
    box-shadow: 0 6px 18px rgba(0,0,0,0.12);
  }

  /* Front */
  .card-front {
    left: 50px;
    background: var(--brand-blue);
    color: var(--white);
    text-align: center;
  }
  .front-tagline {
    position: absolute;
    top: 44px; left: 0; right: 0;
    font-size: 17px;
    line-height: 1.3;
  }
  .front-brand {
    position: absolute;
    top: 128px; left: 0; right: 0;
    display: flex;
    justify-content: center;
    align-items: center;
    gap: 14px;
  }
  .brand-square {
    width: 34px; height: 34px;
    background: currentColor;
  }
  .brand-name {
    font-weight: 700;
    font-size: 30px;
    letter-spacing: 1px;
    text-transform: uppercase;
  }
  .front-invite {
    position: absolute;
    bottom: 40px; left: 0; right: 0;
    font-size: 14px;
  }

  /* Back */
  .card-back {
    left: 625px;
    background: var(--paper);
  }
  .back-panel {
    position: absolute;
    top: 0; right: 0; bottom: 0;
    width: 245px;
    background: var(--panel);
  }
  .back-strip-grey {
    position: absolute;
    left: 0; bottom: 0;
    width: 280px; height: 10px;
    background: var(--ink-mid);
  }
  .back-strip-blue {
    position: absolute;
    right: 0; bottom: 0;
    width: 245px; height: 10px;
    background: var(--brand-blue);
  }
  .back-brand {
    position: absolute;
    top: 38px; left: 30px;
    display: flex;
    align-items: center;
    gap: 10px;
    color: var(--ink-dark);
  }
  .back-brand .brand-square { width: 26px; height: 26px; }
  .back-brand .brand-name { font-size: 22px; }
  .person-name {
    position: absolute;
    top: 122px; left: 30px;
    font-family: "Roboto Condensed", Arial, sans-serif;
    font-weight: 700;
    font-size: 21px;
    color: var(--brand-blue);
  }
  .person-role {
    position: absolute;
    top: 150px; left: 30px;
    font-size: 13px;
    color: var(--ink-dark);
  }
  .contact-list {
    position: absolute;
    top: 182px; left: 30px;
    list-style: none;
    font-size: 14px;
    color: var(--ink-dark);
  }
  .contact-list li {
    display: flex;
    align-items: center;
    gap: 12px;
    height: 22px;
  }
  .contact-list svg { width: 12px; height: 12px; fill: var(--brand-blue); }
  .licence {
    position: absolute;
    top: 110px; right: 40px;
    text-align: left;
    font-size: 13px;
    line-height: 1.35;
    color: var(--ink-mid);
  }
  .licence-numbers { color: var(--brand-blue); font-weight: 500; }
</style>
</head>
<body>

<section class="card card-front">
  <p class="front-tagline">Property Development<br>&amp; Site Acquisition Specialists</p>
  <div class="front-brand">
    <span class="brand-square"></span>
    <span class="brand-name">Kestrel Property Group</span>
  </div>
  <p class="front-invite">Ask me about our INVESTMENT &amp; PARTNERSHIP opportunities</p>
</section>

<section class="card card-back">
  <div class="back-panel"></div>
  <div class="back-strip-grey"></div>
  <div class="back-strip-blue"></div>

  <div class="back-brand">
    <span class="brand-square"></span>
    <span class="brand-name">Kestrel Property Group</span>
  </div>

  <p class="person-name">Daniel Marsh</p>
  <p class="person-role">Director</p>

  <ul class="contact-list">
    <li>
      <svg viewBox="0 0 24 24" aria-hidden="true"><path d="M6.6 10.8a15.1 15.1 0 006.6 6.6l2.2-2.2a1 1 0 011-.25 11.4 11.4 0 003.6.6 1 1 0 011 1V20a1 1 0 01-1 1A17 17 0 013 4a1 1 0 011-1h3.5a1 1 0 011 1c0 1.25.2 2.45.57 3.57a1 1 0 01-.25 1z"/></svg>
      0400 123 456
    </li>
    <li>
      <svg viewBox="0 0 24 24" aria-hidden="true"><path d="M2 5h20v14H2z M2 5l10 8 10-8" stroke="#f4f4f5" stroke-width="1.5"/></svg>
      daniel@kestrelpg.com.au
    </li>
    <li>
      <svg viewBox="0 0 24 24" aria-hidden="true"><circle cx="12" cy="12" r="10"/></svg>
      www.kestrelpg.com.au
    </li>
  </ul>

  <p class="licence">Real Estate Lic:<br><span class="licence-numbers">1234567 &amp; 1234568</span></p>
</section>

</body>
</html>
```